Need a book cover design for a Lumora Book on Herbal Remedies

I need a book cover for my new ebook, here are the details:
Title: Meadow Cures
Sub-Heading: Buried Ancient Garden Tonics
Reclaiming the Wisdom of Roots for Everyday Wellness and Strength
Author: Nora Belcourt

```html
<!DOCTYPE html>
<html lang="en">
<head>
<meta charset="utf-8">
<title>Meadow Cures — Book Cover</title>
<link rel="stylesheet" href="https://fonts.googleapis.com/css2?family=Bebas+Neue&family=EB+Garamond:wght@600;700&family=Great+Vibes&family=Montserrat:wght@800&display=swap">
<style>
  :root {
    --page-bg: #ffffff;
    --title-green: #66cc22;
    --accent-yellow: #f2ff1a;
    --sea-dark: #3e5550;
    --sea-light: #9fb1aa;
    --foam: #c9d0c8;
    --sand: #a89880;
    --sand-dark: #6f6352;
    --leaf: #2f4a2c;
    --spice: #a4582a;
  }
  * { margin: 0; padding: 0; box-sizing: border-box; }
  html, body {
    width: 1200px; height: 900px; overflow: hidden;
    background: var(--page-bg);
  }
  .canvas {
    position: relative; width: 1200px; height: 900px;
    display: flex; align-items: center; justify-content: center;
  }
  .book-cover {
    position: relative; width: 512px; height: 820px; overflow: hidden;
  }
  .cover-art {
    position: absolute; inset: 0;
    background:
      radial-gradient(ellipse 60% 30% at 50% 78%, rgba(164,88,42,0.55), transparent 70%),
      radial-gradient(ellipse 30% 60% at 0% 70%, rgba(47,74,44,0.85), transparent 70%),
      radial-gradient(ellipse 25% 50% at 100% 40%, rgba(47,74,44,0.8), transparent 70%),
      radial-gradient(ellipse 40% 12% at 50% 100%, rgba(47,74,44,0.8), transparent 80%),
      linear-gradient(180deg, var(--sea-dark) 0%, var(--sea-light) 14%, var(--sea-dark) 24%, var(--foam) 36%, var(--sand) 50%, var(--sand-dark) 72%, var(--sand) 90%, var(--sand-dark) 100%);
  }
  .cover-text { position: absolute; left: 0; width: 100%; text-align: center; }
  .subheading {
    top: 40px;
    font-family: "EB Garamond", serif; font-weight: 700;
    font-size: 26px; color: var(--accent-yellow);
  }
  .dot-rule {
    position: absolute; top: 97px; left: 50%; transform: translateX(-50%);
  }
  .title-main {
    top: 150px;
    font-family: "Bebas Neue", sans-serif;
    font-size: 152px; line-height: 1; color: var(--title-green);
  }
  .title-script {
    top: 280px;
    font-family: "Great Vibes", cursive;
    font-size: 112px; line-height: 1.1; color: var(--accent-yellow);
  }
  .tagline {
    top: 450px; left: 50%; width: 300px; margin-left: -150px;
    font-family: "EB Garamond", serif; font-weight: 700;
    font-size: 22px; line-height: 31px; color: var(--accent-yellow);
  }
  .author {
    top: 735px;
    font-family: "Montserrat", sans-serif; font-weight: 800;
    font-size: 34px; letter-spacing: 3px; color: var(--accent-yellow);
  }
</style>
</head>
<body>
<main class="canvas">
  <section class="book-cover">
    <div class="cover-art" role="img" aria-label="Overhead photo of a beach where sea waves wash onto sand, with bowls of herbs, seeds, flowers and spices arranged among tropical leaves"></div>
    <p class="cover-text subheading">Buried Ancient Garden Tonics</p>
    <svg class="dot-rule" width="232" height="12" viewBox="0 0 232 12" aria-hidden="true">
      <g fill="var(--accent-yellow)">
        <circle cx="6" cy="6" r="5"/><circle cx="28" cy="6" r="5"/><circle cx="50" cy="6" r="5"/>
        <circle cx="72" cy="6" r="5"/><circle cx="94" cy="6" r="5"/><circle cx="116" cy="6" r="5"/>
        <circle cx="138" cy="6" r="5"/><circle cx="160" cy="6" r="5"/><circle cx="182" cy="6" r="5"/>
        <circle cx="204" cy="6" r="5"/><circle cx="226" cy="6" r="5"/>
      </g>
    </svg>
    <h1 class="cover-text title-main">MEADOW</h1>
    <p class="cover-text title-script">Cures</p>
    <p class="cover-text tagline">Reclaiming the Wisdom of Roots for Everyday Wellness and Strength</p>
    <p class="cover-text author">NORA BELCOURT</p>
  </section>
</main>
</body>
</html>
```